Zo Fen smart screen Flyer design

Hi,

Please see attached file as I have done up a very very basic flyer just with the information that will need to be presented.

Please don't go with this as a format I would like, as I have no design skills at all.

I'm looking for something that is basic but professional looking capturing this information.
I would prefer if the symbols were changed so they were all consistent and the colour scheme worked together with the logo.

If you can use the picture of the screen provided as I will replace this once my product has its photoshoot.

Thanks!

```html
<!DOCTYPE html>
<html lang="en">
<head>
<meta charset="utf-8">
<title>Zo Fen Smart Screen Flyer</title>
<link rel="stylesheet" href="https://fonts.googleapis.com/css2?family=Open+Sans:wght@400;600;700&display=swap">
<style>
  :root {
    --backdrop: #bfbab4;
    --wall-top: #cdc8c4;
    --wall-mid: #bdb8b4;
    --floor-dark: #4e4d51;
    --ink-dark: #3a3a3c;
    --ink-light: #ffffff;
    --frame: #1d1c1c;
    --screen-warm: #c98a3c;
    --screen-deep: #4a3320;
    --tile: #2b2826;
    --accent: #d9502f;
  }
  * { margin: 0; padding: 0; box-sizing: border-box; }
  html, body { width: 1000px; height: 1200px; overflow: hidden; background: var(--backdrop); }
  body { font-family: "Open Sans", sans-serif; position: relative; }

  .flyer {
    position: absolute; left: 36px; top: 0; width: 928px; height: 1200px;
    overflow: hidden; color: var(--ink-dark);
  }
  .room-photo {
    position: absolute; inset: 0;
    background: linear-gradient(180deg, var(--wall-top) 0%, var(--wall-mid) 50%, #8f8d8e 62%, #646366 75%, var(--floor-dark) 100%);
  }

  .brand { position: absolute; left: 60px; top: 118px; display: flex; align-items: center; gap: 12px; }
  .brand-mark { width: 22px; height: 22px; background: var(--ink-dark); }
  .brand-name { font-size: 48px; font-weight: 600; letter-spacing: 0.04em; color: var(--ink-dark); }

  .intro { position: absolute; left: 60px; top: 236px; width: 380px; }
  .intro p {
    font-size: 16px; line-height: 20.8px; letter-spacing: 0.06em; text-transform: uppercase;
    white-space: nowrap; margin-bottom: 20.8px;
  }

  .display {
    position: absolute; left: 452px; top: 96px; width: 500px; height: 563px;
    background: var(--frame); border-radius: 3px;
  }
  .display-screen {
    position: absolute; left: 18px; top: 17px; right: 0; bottom: 24px;
    background: linear-gradient(160deg, #e9b46a 0%, var(--screen-warm) 25%, #8a5a2a 55%, var(--screen-deep) 100%);
  }
  .screen-brand {
    position: absolute; left: 30px; top: 38px; font-size: 18px; font-weight: 600;
    color: var(--ink-light); letter-spacing: 0.04em;
  }
  .app-tile {
    position: absolute; top: 544px; height: 89px; background: var(--tile);
    display: flex; align-items: center; justify-content: center;
    font-size: 20px; font-weight: 700; color: var(--ink-light);
  }
  .app-tile.is-selected { border: 3px solid #c9c9cf; color: var(--accent); font-size: 24px; }

  .feature { position: absolute; color: var(--ink-light); font-size: 17px; line-height: 25px; }
  .feature-icon { position: absolute; width: 48px; height: 48px; }

  .call { position: absolute; left: 527px; top: 952px; color: var(--ink-light); }
  .call-number { font-size: 33px; font-weight: 700; letter-spacing: 0.08em; line-height: 40px; }
  .call-note { font-size: 16px; font-weight: 700; letter-spacing: 0.55em; margin-top: 2px; }

  .contact {
    position: absolute; left: 0; width: 928px; top: 1069px; text-align: center;
    color: var(--ink-light); font-size: 16px; font-weight: 700; letter-spacing: 0.5em;
  }
  .contact .divider { display: inline-block; width: 2px; height: 20px; background: var(--ink-light); vertical-align: -4px; margin: 0 6px 0 0; }
</style>
</head>
<body>
<main class="flyer">
  <div class="room-photo" role="img" aria-label="Photo of a room interior with a potted palm, a desk with pencils and books, and a wall-mounted screen"></div>

  <header class="brand">
    <span class="brand-mark"></span>
    <span class="brand-name">Zo Fen</span>
  </header>

  <section class="intro">
    <p>Bring attnetion to your bussiness<br>with your own HD LED display.<br>Our displays can be mounted<br>outdoors on walls, roofs, fixed<br>signs, trailer mounted ect.</p>
    <p>We also do indoor LED screens<br>for shop fronts and display<br>stands.</p>
    <p>All screens are cumtom built to<br>your requirements including size,<br>shape and even curved displays</p>
  </section>

  <div class="display">
    <div class="display-screen" role="img" aria-label="Photo of an autumn forest hillside at sunset shown on the screen">
      <span class="screen-brand">Zo Fen</span>
    </div>
  </div>
  <div class="app-tile is-selected" style="left:482px;width:156px;">Moviqo</div>
  <div class="app-tile" style="left:652px;width:130px;">Clipora</div>
  <div class="app-tile" style="left:796px;width:131px;">Storelane</div>

  <svg class="feature-icon" style="left:44px;top:733px;" viewBox="0 0 48 48" aria-hidden="true">
    <text x="2" y="16" fill="#fff" font-family="Open Sans, sans-serif" font-size="13">4G</text>
    <rect x="2" y="36" width="6" height="8" rx="2" fill="#fff"/>
    <rect x="11" y="30" width="6" height="14" rx="2" fill="#fff"/>
    <rect x="20" y="24" width="6" height="20" rx="2" fill="#fff"/>
    <rect x="29" y="14" width="7" height="30" rx="2" fill="#fff"/>
  </svg>
  <p class="feature" style="left:114px;top:736px;width:320px;">Change screen content with a click of the mouse anywhere in the world</p>

  <svg class="feature-icon" style="left:44px;top:825px;" viewBox="0 0 48 48" aria-hidden="true">
    <circle cx="24" cy="24" r="10" fill="none" stroke="#fff" stroke-width="3"/>
    <path d="M24 14 A10 10 0 0 1 24 34 Z" fill="#fff"/>
    <g stroke="#fff" stroke-width="3" stroke-linecap="round">
      <line x1="24" y1="2" x2="24" y2="8"/><line x1="24" y1="40" x2="24" y2="46"/>
      <line x1="2" y1="24" x2="8" y2="24"/><line x1="40" y1="24" x2="46" y2="24"/>
      <line x1="8" y1="8" x2="12" y2="12"/><line x1="36" y1="36" x2="40" y2="40"/>
      <line x1="40" y1="8" x2="36" y2="12"/><line x1="8" y1="40" x2="12" y2="36"/>
    </g>
  </svg>
  <p class="feature" style="left:124px;top:823px;width:320px;">Screen will automatically adjust to suit ambiant light improving screen veiwing quality and saving in power consumption</p>

  <svg class="feature-icon" style="left:44px;top:948px;" viewBox="0 0 48 48" aria-hidden="true">
    <circle cx="24" cy="24" r="21" fill="none" stroke="#fff" stroke-width="3"/>
    <circle cx="24" cy="24" r="14" fill="none" stroke="#fff" stroke-width="3"/>
  </svg>
  <p class="feature" style="left:122px;top:957px;width:320px;">Setting high standard for colour, brightness and sharpness these LED modules will create attention.</p>

  <svg class="feature-icon" style="left:490px;top:730px;" viewBox="0 0 48 48" aria-hidden="true">
    <g fill="none" stroke="#fff" stroke-width="4" stroke-linecap="round">
      <path d="M4 18 Q24 2 44 18"/><path d="M11 25 Q24 14 37 25"/><path d="M18 32 Q24 27 30 32"/>
    </g>
    <circle cx="24" cy="39" r="3.5" fill="#fff"/>
  </svg>
  <p class="feature" style="left:569px;top:724px;width:316px;">Change screen content with a PC, tablet or mobile phone with an easy to use<br>app</p>

  <svg class="feature-icon" style="left:490px;top:846px;" viewBox="0 0 48 48" aria-hidden="true">
    <g fill="none" stroke="#fff" stroke-width="3">
      <rect x="2" y="4" width="44" height="30" rx="1"/>
      <line x1="2" y1="29" x2="46" y2="29"/>
      <line x1="20" y1="34" x2="20" y2="42"/><line x1="28" y1="34" x2="28" y2="42"/>
      <line x1="12" y1="43" x2="36" y2="43"/>
    </g>
  </svg>
  <p class="feature" style="left:569px;top:838px;width:330px;">Monitor cabinet temperature and humidity plus more in real time online. Recieve alerts via email.</p>

  <div class="call">
    <div class="call-number">1300 ZOFENWA</div>
    <div class="call-note">FOR A FREE QUOTE</div>
  </div>

  <footer class="contact">WWW.ZOFENWA.COM.AU <span class="divider"></span> INFO@ZOFENWA.COM.AU</footer>
</main>
</body>
</html>
```